Business card design needed

We are an electrical Contracting Company with a solar power division and Air conditioning
Our primary business is Solar PV, Solar Hot water, Electrical Maintenance, Repairs, and installs. Air Conditioning Installation is also one of our areas,
My Web Site is: www.tolvexenergy.com
and www.derrickhollowayelectrical.com.au.
If we could incorporate the back feature photos on the tolvexenergy website that would help resemble our vehicles help the customers remember us.

Cheers
Derrick
0427591368

Electrical

tolvexenergy.com electrical contractors
a division of Derrick Holloway Electrical P/L
22/5 Pelner Court
Corrimal Flats Q 4231
Phone: 0427591368
Office: 0763048215
Fax: 0763048790
email: dhwpower@voltmailer.com
Website: www.tolvexenergy.com
www.derrickhollowayelectrical.com.au
License number: Q71293,KPN B2084715, NSW 63912D,TVU M047182

```html
<!DOCTYPE html>
<html lang="en">
<head>
<meta charset="utf-8">
<title>Tolvex Energy – Business Card</title>
<link rel="stylesheet" href="https://fonts.googleapis.com/css2?family=Arimo:wght@400;700&display=swap">
<style>
  :root{
    --page:#ffffff;
    --frame:#e3e3e3;
    --sky:#eef5f8;
    --haze:#e4ecd9;
    --meadow-light:#b7d07a;
    --meadow:#7aa23c;
    --meadow-deep:#4f7826;
    --orange:#ef6a1c;
    --white:#ffffff;
    --ink:#2b2b2b;
    --ink-soft:#3c3c3c;
    --panel:rgba(255,255,255,0.62);
    --shadow:rgba(0,0,0,0.22);
  }
  *{margin:0;padding:0;box-sizing:border-box}
  html,body{width:1200px;height:436px;overflow:hidden;background:var(--page)}
  body{font-family:"Arimo",Arial,sans-serif;position:relative}
  .canvas-frame{position:absolute;inset:0;border:1px solid var(--frame)}
  .card{
    position:absolute;top:68px;width:532px;height:308px;border-radius:22px;overflow:hidden;
    box-shadow:0 6px 14px var(--shadow);
  }
  .card--front{left:52px}
  .card--back{left:620px}
  .meadow-photo{
    position:absolute;inset:0;
    background:linear-gradient(180deg, var(--sky) 0%, var(--haze) 30%, var(--meadow-light) 55%, var(--meadow) 80%, var(--meadow-deep) 100%);
  }
  .txt{position:absolute;white-space:nowrap}
  .tagline{left:98px;top:38px;font-size:11px;color:var(--ink)}
  .brand-name{left:98px;top:62px;font-size:26px;font-weight:700;color:var(--white)}
  .headline{left:28px;top:144px;font-size:21px;font-weight:700;color:var(--orange);letter-spacing:.2px}
  .division{left:30px;top:186px;font-size:11px;font-weight:700;color:var(--white)}
  .front-web{left:95px;top:246px;font-size:15px;font-weight:700;color:var(--white)}

  .contact-panel{
    position:absolute;left:160px;top:42px;width:348px;height:244px;border-radius:12px;background:var(--panel);
  }
  .holder-name{left:182px;top:53px;font-size:12px;font-weight:700;color:var(--ink)}
  .contact-list{position:absolute;left:176px;top:80px;list-style:none}
  .contact-list li{display:flex;align-items:flex-start;gap:8px;font-size:14.5px;color:var(--ink-soft);line-height:18px;margin-bottom:4px}
  .contact-list li.multi span{line-height:22px;margin-top:-2px}
  .contact-list li.multi{margin-bottom:2px}
  .contact-list svg{width:16px;height:16px;flex:0 0 16px;margin-top:1px;fill:none;stroke:var(--ink-soft);stroke-width:1.4}
  .license{left:186px;top:245px;font-size:11px;color:var(--ink-soft);line-height:18px}
</style>
</head>
<body>
<div class="canvas-frame"></div>

<section class="card card--front">
  <div class="meadow-photo" role="img" aria-label="Photo of a large white daisy in a sunlit meadow of flowers and grass"></div>
  <p class="txt tagline">Gold Coast Solar Panels!</p>
  <p class="txt brand-name">tolvexenergy.com</p>
  <p class="txt headline">ELECTRICAL CONTRACTORS</p>
  <p class="txt division">A DIVISION OF DERRICK HOLLOWAY ELECTRICAL</p>
  <p class="txt front-web">www.tolvexenergy.com</p>
</section>

<section class="card card--back">
  <div class="meadow-photo" role="img" aria-label="Photo of a white daisy in a sunlit meadow, continuing from the front"></div>
  <div class="contact-panel"></div>
  <p class="txt holder-name">DERRICK HOLLOWAY</p>
  <ul class="contact-list">
    <li><svg viewBox="0 0 16 16"><rect x="4" y="1.5" width="8" height="13" rx="1.3"/><line x1="7" y1="12.3" x2="9" y2="12.3"/></svg>0427591368</li>
    <li><svg viewBox="0 0 16 16"><path d="M3 2.5l2.5-.5 1.5 3-1.5 1.2a8 8 0 0 0 3.8 3.8L10.5 8.5l3 1.5-.5 2.5c-5 1-11-5-10-10z" fill="var(--ink-soft)" stroke="none"/></svg>0763048215</li>
    <li><svg viewBox="0 0 16 16"><rect x="4" y="2" width="8" height="4"/><rect x="2" y="6" width="12" height="6" rx="1"/><rect x="4" y="10" width="8" height="4"/></svg>0763048790</li>
    <li><svg viewBox="0 0 16 16"><rect x="1.5" y="3.5" width="13" height="9"/><path d="M1.5 3.5l6.5 5 6.5-5"/></svg>dhwpower@voltmailer.com</li>
    <li class="multi"><svg viewBox="0 0 16 16"><circle cx="8" cy="8" r="6.3"/><ellipse cx="8" cy="8" rx="2.8" ry="6.3"/><line x1="1.7" y1="8" x2="14.3" y2="8"/></svg><span>www.tolvexenergy.com<br>www.derrickhollowayelectrical.com.au</span></li>
    <li><svg viewBox="0 0 16 16"><path d="M8 14.5s-4.5-4.8-4.5-8a4.5 4.5 0 0 1 9 0c0 3.2-4.5 8-4.5 8z"/><circle cx="8" cy="6.5" r="1.6"/></svg>P/L 22/5 Pelner Court Corrimal Flats Q 4231</li>
  </ul>
  <p class="txt license">License number:<br>Q71293,KPN B2084715, NSW 63912D,TVU M047182</p>
</section>
</body>
</html>
```